redesign corporate website (software courses)

We need a complete redesign of the current website: http://q-o-r.biz/ (training: http://q-o-r.biz/pt-br/treinamento/web ); more clear, different color, navigation, header, footer, whatever (side note: site will be based on bootstrap and drupal). Most important pages:

http://q-o-r.biz/pt-br/treinamento (trainingoverviewpage)
http://q-o-r.biz/ (frontpage)
http://q-o-r.biz/pt-br/treinamento/web (trianingdetailpage)

The design should be valid for further content pages (like http://q-o-r.biz/pt-br/desenvolvimentodesoftware) and pages with forms (http://q-o-r.biz/pt-br/contact or http://q-o-r.biz/pt-br/training/web/register)

Logo attached in white and black and black with shadow.

Some other examples of training sites (just content examples - not as template for similar layout):

http://www.brivatutor.example/packages/4817/Website-Development-Professional-training.html?advid=31&gclid=XQa93pLmw42HGtrk5BsjEZWKpR
http://www.code-lehrhaus.example/
http://www.devalto.example/cursos/kestrel-framework-ii/
http://www.varnholt-academy.example/lp/php-development-training.aspx?gclid=MT3hwqUvb52DJYRR8Bpexk9B7B

Industry/Entity Type

Software

```html
<!DOCTYPE html>
<html lang="en">
<head>
<meta charset="utf-8">
<title>QOR Software Academy – Training</title>
<link href="https://fonts.googleapis.com/css2?family=Roboto:wght@400;500;700&family=Roboto+Condensed:wght@700&display=swap" rel="stylesheet">
<style>
  :root {
    --orange: #f15a1d;
    --orange-dark: #e04e12;
    --ink: #1f1f1f;
    --text: #4a4a4a;
    --muted: #8a8a8a;
    --band: #f1f1f1;
    --line: #e3e3e3;
    --white: #ffffff;
  }
  * { box-sizing: border-box; margin: 0; padding: 0; }
  html, body { width: 843px; height: 1200px; overflow: hidden; }
  body { position: relative; background: var(--white); font-family: "Roboto", Arial, sans-serif; color: var(--text); }
  .abs { position: absolute; }

  /* header */
  .top-rule { left: 0; top: 0; width: 843px; height: 3px; background: var(--orange); }
  .site-header { left: 0; top: 3px; width: 843px; height: 67px; background: var(--white); border-bottom: 1px solid var(--line); }
  .brand { left: 78px; display: flex; align-items: center; gap: 8px; }
  .brand-dot { width: 34px; height: 34px; border-radius: 50%; background: var(--orange); }
  .brand-name { font-weight: 700; font-size: 15px; line-height: 1.05; color: var(--ink); letter-spacing: .5px; }
  .main-nav { left: 372px; display: flex; gap: 27px; font-size: 10px; color: var(--ink); letter-spacing: .2px; }
  .main-nav .active { color: var(--orange); }
  .search { left: 634px; width: 131px; height: 17px; border: 1px solid var(--line); background: #f8f8f8; font-size: 6.5px; color: var(--muted); padding: 4px 5px; }

  /* hero */
  .hero { left: 0; top: 70px; width: 843px; height: 348px; background: linear-gradient(90deg, #5b4b3f 0%, #9a8675 22%, #c9b7a4 45%, #a8988a 65%, #4a4643 100%); }
  .hero-panel { left: 85px; top: 197px; width: 366px; height: 184px; background: rgba(150,150,150,.55); }
  .hero-title { left: 96px; top: 205px; font-family: "Roboto Condensed", "Roboto", sans-serif; font-weight: 700; font-size: 30px; color: var(--ink); }
  .ribbon { left: 85px; width: 349px; height: 25px; background: var(--orange); color: var(--white); font-size: 13.5px; display: flex; align-items: center; padding-left: 10px; gap: 8px; clip-path: polygon(0 0, 100% 0, 94% 100%, 0 100%); }
  .ribbon-dot { width: 14px; height: 14px; border-radius: 50%; border: 2px solid var(--white); background: rgba(255,255,255,.3); }

  .enquire-head { left: 589px; top: 130px; width: 157px; height: 46px; background: var(--orange); color: var(--white); font-family: "Roboto Condensed", sans-serif; font-weight: 700; font-size: 17px; line-height: 19px; padding: 5px 14px; }
  .enquire-body { left: 589px; top: 176px; width: 157px; height: 206px; background: rgba(160,160,160,.72); }
  .field { left: 597px; width: 141px; height: 19px; background: var(--white); border: 1px solid #ddd; font-size: 6.5px; color: #666; padding: 5px 9px; }
  .field.tall { height: 39px; line-height: 8px; padding-top: 7px; }
  .captcha-box { left: 662px; top: 332px; width: 54px; height: 15px; background: #dcebd8; font-size: 10px; color: #333; padding: 1px 4px; letter-spacing: .5px; }
  .btn { background: var(--orange); color: var(--white); font-size: 8px; text-align: center; line-height: 15px; height: 15px; }
  .enquire-btn { left: 598px; top: 356px; width: 51px; }

  /* intro */
  .intro-col { top: 452px; width: 334px; border-left: 4px solid var(--orange); padding-left: 9px; height: 122px; }
  .intro-col h2 { font-weight: 400; font-size: 18px; color: var(--ink); margin-bottom: 8px; margin-top: -3px; }
  .intro-col p { font-size: 6.4px; line-height: 12px; color: var(--text); }
  .intro-col .btn { position: absolute; left: 9px; bottom: 0; width: 52px; }

  /* what we do / servicing */
  .band { left: 0; top: 592px; width: 843px; height: 277px; background: var(--band); }
  .section-title { font-weight: 400; font-size: 17px; color: var(--ink); }
  .do-item { left: 78px; width: 330px; height: 43px; background: var(--white); display: flex; }
  .do-plus { width: 25px; height: 43px; background: var(--orange); color: var(--white); font-size: 26px; line-height: 41px; text-align: center; font-weight: 300; }
  .do-item p { font-size: 6.8px; line-height: 8.8px; padding: 9px 10px 0 16px; }
  .serv-icon { left: 430px; width: 60px; height: 60px; border-radius: 50%; background: var(--white); border: 1px solid var(--line); display: flex; align-items: center; justify-content: center; }
  .serv-text { left: 496px; width: 272px; }
  .serv-text h3 { font-size: 6.8px; font-weight: 700; color: var(--ink); margin-bottom: 3px; }
  .serv-text p { font-size: 6.8px; line-height: 8.8px; }

  /* contact + testimonial */
  .contact-row { left: 78px; width: 285px; display: flex; gap: 10px; font-size: 10.5px; color: var(--ink); align-items: flex-start; white-space: nowrap; }
  .contact-row .link { color: var(--orange); line-height: 13px; }
  .quote-disc { left: 373px; top: 883px; width: 104px; height: 104px; border-radius: 50%; background: var(--orange); color: var(--white); font-size: 84px; font-weight: 700; line-height: 1; padding: 28px 0 0 10px; }
  .portrait { left: 430px; top: 885px; width: 100px; height: 100px; border-radius: 50%; background: radial-gradient(circle at 45% 45%, #d9b9a2, #a07e68 60%, #e7e7e7 100%); }
  .quote-text { left: 542px; top: 909px; width: 220px; font-size: 6.8px; line-height: 8.8px; }
  .quote-name { left: 542px; top: 973px; font-size: 7.5px; font-weight: 700; color: var(--ink); }

  /* footer */
  .site-footer { left: 0; top: 1016px; width: 843px; height: 184px; background: var(--orange); color: var(--white); text-align: center; }
  .site-footer h2 { position: absolute; top: 28px; width: 100%; font-size: 18px; font-weight: 700; }
  .site-footer .lede { position: absolute; top: 50px; width: 100%; font-size: 7.6px; line-height: 10px; }
  .social { position: absolute; top: 82px; left: 383px; display: flex; gap: 9px; }
  .social span { width: 13px; height: 13px; border-radius: 50%; background: var(--white); }
  .footer-nav { position: absolute; top: 106px; width: 100%; display: flex; justify-content: center; gap: 15px; font-size: 9.5px; }
  .footer-brand { position: absolute; top: 130px; left: 360px; display: flex; align-items: center; gap: 6px; }
  .footer-brand .brand-dot { width: 24px; height: 24px; background: var(--white); }
  .footer-brand .brand-name { color: var(--white); font-size: 10px; }
</style>
</head>
<body>
  <div class="abs top-rule"></div>
  <header class="abs site-header">
    <div class="abs brand" style="top:12px">
      <span class="brand-dot"></span>
      <span class="brand-name">QOR<br>SOFTWARE ACADEMY</span>
    </div>
    <nav class="abs main-nav" style="top:28px">
      <span class="active">HOME</span><span>TRAINING</span><span>SERVICING</span><span>CONTACT</span>
    </nav>
    <div class="abs search" style="top:25px">Enter your search...</div>
  </header>

  <section class="abs hero" role="img" aria-label="Photo of smiling students working at computers in a classroom"></section>
  <div class="abs hero-panel"></div>
  <h1 class="abs hero-title">Learn web development</h1>
  <div class="abs ribbon" style="top:249px"><span class="ribbon-dot"></span>Lorem ipsum dolor sit amet, consectetur adipisci</div>
  <div class="abs ribbon" style="top:282px"><span class="ribbon-dot"></span>Lorem ipsum dolor sit amet, consectetur adipisci</div>
  <div class="abs ribbon" style="top:315px"><span class="ribbon-dot"></span>Lorem ipsum dolor sit amet, consectetur adipisci</div>
  <div class="abs ribbon" style="top:346px"><span class="ribbon-dot"></span>Lorem ipsum dolor sit amet, consectetur adipisci</div>

  <div class="abs enquire-head">Enquire Now for<br>Training</div>
  <div class="abs enquire-body"></div>
  <div class="abs field" style="top:187px">Name</div>
  <div class="abs field" style="top:212px">Email</div>
  <div class="abs field" style="top:236px">Phone</div>
  <div class="abs field" style="top:261px">Select Country<span style="float:right">&#9662;</span></div>
  <div class="abs field tall" style="top:284px">Enter Counse Deatil and Preferred<br>Month</div>
  <div class="abs field" style="top:332px;width:59px;height:16px;padding-top:4px">Enter Coade</div>
  <div class="abs captcha-box">B26SP</div>
  <div class="abs btn enquire-btn">Enquire</div>

  <section class="abs intro-col" style="left:78px">
    <h2>WELCOME!</h2>
    <p>Aenean quis quam quis ipsum volutpat rutrum. Nam ultrices, tellus at viverra rutrum, massa nibh placerat est, a venenatis lorem neque et lectus. Nullam quis tortor sed nunc convallis blandit. Vestibulum sit amet urna sit amet arcu venenatis commodo ac et ligula. Cras rutrum quam eget velit aliquam hendrerit. Mauris sed massa ligula. Suspendisse at velit ac erat lobortis. Praesent vestibulum metus ac felis vehicula, at feugiat turpis pellentesque. Nullam nec nunc accumsan, accumsan nibh vel, varius erat.</p>
    <div class="btn">Enquire</div>
  </section>
  <section class="abs intro-col" style="left:430px">
    <h2>ABOUT US</h2>
    <p>Aenean quis quam quis ipsum volutpat rutrum. Nam ultrices, tellus at viverra rutrum, massa nibh placerat est, a venenatis lorem neque et lectus. Nullam quis tortor sed nunc convallis blandit. Vestibulum sit amet urna sit amet arcu venenatis commodo ac et ligula. Cras rutrum quam eget velit aliquam hendrerit. Mauris sed massa ligula. Suspendisse at velit ac erat lobortis. Praesent vestibulum metus ac felis vehicula, at feugiat turpis pellentesque. Nullam nec nunc accumsan, accumsan nibh vel, varius erat.</p>
    <div class="btn">Enquire</div>
  </section>

  <div class="abs band"></div>
  <h2 class="abs section-title" style="left:78px;top:616px">WHAT WE DO</h2>
  <h2 class="abs section-title" style="left:430px;top:617px">OUR SERVICING</h2>

  <div class="abs do-item" style="top:649px"><div class="do-plus">+</div><p>Nulla facilisi. Suspendisse gravida arcu eget iaculis accumsan. Sed pretium, felis at hendrerit porta, risus odio porta purus, eu viverra tortor turpis in erat. Integer hendrerit arcu quis eros bibendum.</p></div>
  <div class="abs do-item" style="top:699px"><div class="do-plus">+</div><p>Nulla facilisi. Suspendisse gravida arcu eget iaculis accumsan. Sed pretium, felis at hendrerit porta, risus odio porta purus, eu viverra tortor turpis in erat. Integer hendrerit arcu quis eros bibendum.</p></div>
  <div class="abs do-item" style="top:749px"><div class="do-plus">+</div><p>Nulla facilisi. Suspendisse gravida arcu eget iaculis accumsan. Sed pretium, felis at hendrerit porta, risus odio porta purus, eu viverra tortor turpis in erat. Integer hendrerit arcu quis eros bibendum.</p></div>
  <div class="abs do-item" style="top:799px"><div class="do-plus">+</div><p>Nulla facilisi. Suspendisse gravida arcu eget iaculis accumsan. Sed pretium, felis at hendrerit porta, risus odio porta purus, eu viverra tortor turpis in erat. Integer hendrerit arcu quis eros bibendum.</p></div>

  <div class="abs serv-icon" style="top:652px">
    <svg width="34" height="30" viewBox="0 0 34 30" fill="none" stroke="#222" stroke-width="2"><circle cx="11" cy="9" r="5"/><circle cx="11" cy="9" r="1.5" fill="#222"/><rect x="14" y="15" width="16" height="11" rx="1"/><line x1="2" y1="28" x2="32" y2="28"/></svg>
  </div>
  <div class="abs serv-text" style="top:657px"><h3>Suspendisse gravida arcu eget iaculis accumsan</h3><p>Nulla facilisi. Suspendisse gravida arcu eget iaculis accumsan. Sed pretium, felis at hendrerit porta, risus odio porta purus, eu viverra tortor turpis in erat. Integer hendrerit arcu quis eros bibendum.</p></div>

  <div class="abs serv-icon" style="top:716px">
    <svg width="32" height="32" viewBox="0 0 32 32" fill="none" stroke="#222" stroke-width="2"><circle cx="15" cy="15" r="12"/><ellipse cx="15" cy="15" rx="5" ry="12"/><line x1="3" y1="15" x2="27" y2="15"/><line x1="5" y1="9" x2="25" y2="9"/><line x1="5" y1="21" x2="25" y2="21"/></svg>
  </div>
  <div class="abs serv-text" style="top:727px"><h3>Suspendisse gravida arcu eget iaculis accumsan</h3><p>Nulla facilisi. Suspendisse gravida arcu eget iaculis accumsan. Sed pretium, felis at hendrerit porta, risus odio porta purus, eu viverra tortor turpis in erat. Integer hendrerit arcu quis eros bibendum.</p></div>

  <div class="abs serv-icon" style="top:780px">
    <svg width="30" height="28" viewBox="0 0 30 28" fill="none" stroke="#222" stroke-width="2"><rect x="3" y="3" width="24" height="20" rx="2"/><line x1="8" y1="9" x2="22" y2="9"/><line x1="8" y1="13" x2="22" y2="13"/><line x1="8" y1="17" x2="16" y2="17"/></svg>
  </div>
  <div class="abs serv-text" style="top:792px"><h3>Suspendisse gravida arcu eget iaculis accumsan</h3><p>Nulla facilisi. Suspendisse gravida arcu eget iaculis accumsan. Sed pretium, felis at hendrerit porta, risus odio porta purus, eu viverra tortor turpis in erat. Integer hendrerit arcu quis eros bibendum.</p></div>

  <div class="abs contact-row" style="top:917px">
    <svg width="14" height="14" viewBox="0 0 14 14" fill="none" stroke="#555" stroke-width="1.2"><path d="M7 13 C3 8 2.5 6.5 2.5 5 a4.5 4.5 0 0 1 9 0 c0 1.5 -.5 3 -4.5 8z"/><circle cx="7" cy="5" r="1.6"/></svg>
    <span>USA – Fairmont, 418 Alder Street, CA 90512</span>
  </div>
  <div class="abs contact-row" style="top:943px">
    <svg width="14" height="12" viewBox="0 0 14 12" fill="none" stroke="#555" stroke-width="1.2"><rect x="1" y="2" width="12" height="8"/><path d="M1 2 L7 7 L13 2"/></svg>
    <span class="link">link@qor-academy.example</span>
  </div>
  <div class="abs contact-row" style="top:970px">
    <svg width="14" height="14" viewBox="0 0 14 14" fill="none" stroke="#555" stroke-width="1.2"><path d="M3 1.5 L5.5 4 L4 6 C5 8 6 9 8 10 L10 8.5 L12.5 11 L11 12.5 C6 12 2 8 1.5 3z"/></svg>
    <span class="link">0800 555 0141<br>0800 555 0142</span>
  </div>

  <div class="abs quote-disc">&ldquo;</div>
  <div class="abs portrait" role="img" aria-label="Portrait photo of a grey-haired client giving a testimonial"></div>
  <p class="abs quote-text">Nulla facilisi. Suspendisse gravida arcu eget iaculis accumsan. Sed pretium, felis at hendrerit porta, risus odio porta purus, eu viverra tortor turpis in erat. Integer hendrerit arcu quis eros bibendum. Sed pretium, felis at hendrerit porta, risus odio porta purus, eu viverra tortor turpis in erat. &rdquo;</p>
  <p class="abs quote-name">Yspendisse gravi</p>

  <footer class="abs site-footer">
    <h2>GET IN TOUCH</h2>
    <p class="lede">Nulla facilisi. Suspendisse gravida arcu eget iaculis accumsan. Sed pretium, felis at hendrerit porta,<br>risus odio porta purus, eu viverra tortor turpis in erat. Integer hendrerit arcu quis eros bibendum,</p>
    <div class="social" aria-label="Social links"><span></span><span></span><span></span><span></span></div>
    <nav class="footer-nav"><span>HOME</span><span>TRAINING</span><span>SERVICING</span><span>CONTACT</span></nav>
    <div class="footer-brand"><span class="brand-dot"></span><span class="brand-name">QOR<br>SOFTWARE ACADEMY</span></div>
  </footer>
</body>
</html>
```